Create a modifyable PDF

Hello,

We have a three modifiable PDF's which have been designed in Illustrator that require updating. Two documents require a complete replacement of the text while the 3rd document has minor changes.
Updates

I have attached two examples of the minor changes to 1 PDF document and a sample of the PDF where the content needs to be updated from a word document.

```html
<!DOCTYPE html>
<html lang="en">
<head>
<meta charset="utf-8">
<title>Loan Note (Lump Sum Note)</title>
<link href="https://fonts.googleapis.com/css2?family=Arimo:wght@700&family=Source+Sans+3:wght@400;700&display=swap" rel="stylesheet">
<style>
  :root {
    --brand-orange: #f15a29;
    --ink: #231f20;
    --paper: #ffffff;
    --rule: #231f20;
  }
  * { box-sizing: border-box; margin: 0; padding: 0; }
  html, body { width: 927px; height: 1200px; overflow: hidden; background: var(--paper); }
  .page {
    position: relative; width: 927px; height: 1200px; overflow: hidden;
    font-family: "Source Sans 3", "Myriad Pro", sans-serif;
    color: var(--ink); background: var(--paper);
  }
  .band { position: absolute; left: 0; width: 100%; height: 12px; background: var(--brand-orange); }
  .band--top { top: 0; }
  .band--bottom { bottom: 0; }

  .brand { position: absolute; left: 74px; top: 60px; display: flex; align-items: center; gap: 8px; }
  .brand__dot { width: 14px; height: 14px; border-radius: 50%; background: var(--brand-orange); }
  .brand__name { font-family: "Source Sans 3", sans-serif; font-weight: 700; font-size: 26px; color: var(--brand-orange); letter-spacing: 0.2px; }

  .doc-title {
    position: absolute; top: 154px; left: 0; width: 100%; text-align: center;
    font-family: "Arimo", Arial, sans-serif; font-weight: 700; font-size: 17.5px;
  }

  .clause {
    position: absolute; left: 67px; width: 795px;
    font-size: 15px; line-height: 19.6px; text-align: justify;
  }
  .clause--intro { top: 199px; }
  .clause--loan { top: 360px; }
  .clause--claim { top: 659px; }
  .clause--repay { top: 961px; }
  .clause__num { display: inline-block; width: 53px; }
  .clause b { font-weight: 700; }

  .blank { display: inline-block; border-bottom: 1px solid var(--rule); height: 14px; vertical-align: baseline; }

  .claim-details { position: absolute; left: 170px; top: 832px; }
  .claim-details__row { display: flex; align-items: flex-end; height: 40px; font-size: 14px; font-weight: 700; }
  .claim-details__label { width: 108px; }
  .claim-details__colon { width: 24px; }
  .claim-details__line { width: 456px; border-bottom: 1px solid var(--rule); height: 14px; margin-bottom: 2px; }

  .footer {
    position: absolute; top: 1106px; left: 0; width: 100%; font-size: 14px; line-height: 19px;
  }
  .footer__web { position: absolute; left: 79px; top: 2px; }
  .footer__address { position: absolute; left: 262px; width: 405px; text-align: center; }
  .footer__phone { position: absolute; left: 735px; top: 2px; display: flex; align-items: center; gap: 4px; }
  .footer__divider { position: absolute; top: 6px; width: 1px; height: 18px; background: var(--ink); }
  .footer__divider--left { left: 255px; }
  .footer__divider--right { left: 672px; }
</style>
</head>
<body>
<div class="page">
  <div class="band band--top"></div>

  <div class="brand">
    <span class="brand__dot"></span>
    <span class="brand__name">Clearway Claim Funding Inc.</span>
  </div>

  <h1 class="doc-title">LOAN NOTE (LUMP SUM NOTE)</h1>

  <p class="clause clause--intro">This <b>LOAN NOTE</b> dated effective the <span class="blank" style="width:62px"></span> day of <span class="blank" style="width:150px"></span> , 20 <span class="blank" style="width:42px"></span> , between <span class="blank" style="width:112px"></span> <span class="blank" style="width:228px"></span> , an individual residing in <span class="blank" style="width:242px"></span>, in the Province of <span class="blank" style="width:170px"></span> (hereinafter referred to as the <b>“Borrower”</b>) and <b>CLEARWAY CLAIM FUNDING INC.</b>, a corporation incorporated under the laws of Canada (hereinafter referred to as the “Lender”) witnesses that, in consideration of the premises, agreements and obligations herein set forth and other good and valuable consideration which the parties hereto conclusively acknowledge, the parties hereto covenant and agree as follows:</p>

  <p class="clause clause--loan"><span class="clause__num">1.</span>Subject to the terms and conditions of this Agreement, the Lender agrees to provide to the Borrower a loan (the <b>“Loan”</b>) equal to the amount of $ <span class="blank" style="width:182px"></span> (the <b>“Principal Sum”</b>). The Borrower hereby acknowledges itself indebted and promises to pay to or to the order of the Lender in lawful money of Canada the Loan plus interest (<b>“Interest”</b>) at a rate of 24% per annum compounded semi-annually until paid (<b>“Interest Rate”</b>), computed from the date of advance of the Principal Sum to the date of repayment of the Loan (the <b>“Payment Date”</b>). Interest shall be accrued on a daily basis by applying the Interest Rate to the Principal Sum. Notwithstanding any of the foregoing to the contrary, the Borrower hereby agrees that a minimum of six (6) months of Interest shall apply on the Principal Sum (<b>“Minimum Interest”</b>) even if the Payment Date occurs within six (6) months of the date of the advance of the Principal Sum. Other than the Interest, the only other fees in respect of this Loan payable by the Borrower is an administration fee of $375 plus applicable taxes (the <b>“Administration Fee”</b>). The Borrower agrees that the Administration Fee shall be paid by the Borrower out of the Principal Sum advanced under this Loan and that the Lender shall be entitled to deduct the Administration Fee out of the money advanced to the Borrower under this Loan. The effective annual interest rate (<b>“APR”</b>) is <span class="blank" style="width:84px"></span> %. The attached Statement of Disclosure forms a part of this Loan Note.</p>

  <p class="clause clause--claim"><span class="clause__num">2.</span>The Loan is being provided directly to the Borrower who is a plaintiff in the following legal claim (the <b>“Claim”</b>). In the event of a change in the Borrower’s legal counsel related to the Claim, the Borrower shall promptly notify the Lender within five (5) days of such change of counsel and provide to the Lender, at the Borrower’s expense, an Irrevocable Authorization and Direction naming the new counsel and a Certification and Lawyer Acknowledgement from such new counsel (the <b>“Change of Counsel Documents”</b>). The Loan shall not be used by the Borrower to pay for lawyer’s fees, expert fees, costs or other litigation expenses related to the Borrower’s Claim (<b>“Use of Funds Commitment”</b>).</p>

  <div class="claim-details">
    <div class="claim-details__row"><span class="claim-details__label">Style of Cause</span><span class="claim-details__colon">:</span><span class="claim-details__line"></span></div>
    <div class="claim-details__row"><span class="claim-details__label">Name of Court</span><span class="claim-details__colon">:</span><span class="claim-details__line"></span></div>
    <div class="claim-details__row"><span class="claim-details__label">Court File No.</span><span class="claim-details__colon">:</span><span class="claim-details__line"></span></div>
  </div>

  <p class="clause clause--repay"><span class="clause__num">3.</span>Subject to an Event of Default (as hereinafter defined), the Loan and Interest shall only be repayable by the Borrower to the Lender if the Borrower recovers any Proceeds (as hereinafter defined) from the Claim (the <b>“Repayment Obligation”</b>).</p>

  <footer class="footer">
    <span class="footer__web">www.clearwayfunding.ca</span>
    <span class="footer__divider footer__divider--left"></span>
    <span class="footer__address">Harbourline Tower, 240 Front Street, 14th Floor<br>PO Box 312 Toronto, Ontario M5V 1A4</span>
    <span class="footer__divider footer__divider--right"></span>
    <span class="footer__phone">
      <svg width="16" height="13" viewBox="0 0 16 13" aria-hidden="true">
        <rect x="1" y="5" width="14" height="7.5" rx="1" fill="none" stroke="#231f20" stroke-width="1"/>
        <path d="M0.5 4.5 Q8 -1 15.5 4.5 L13 6 L11 4 Q8 3 5 4 L3 6 Z" fill="#231f20"/>
        <circle cx="8" cy="8.7" r="2" fill="none" stroke="#231f20" stroke-width="1"/>
      </svg>
      1-866-555-0148
    </span>
  </footer>

  <div class="band band--bottom"></div>
</div>
</body>
</html>
```